Large Signage - Graphics for 5m x 3m wall to vinyl wrap

Wanting a graphic / sign design for an internal wall within an ict business.

We have a 5m long by 3m high wall we want to put a vinyl wrap graphic on it to provide a good visual in the store and show the concept of what we do.

We are a varied ict business that specialises in fleet vehicle tracking, mobile phone car kits, IT managed services, data and network cabling, mobile phone coverage extenders, M2M, digital marketing, cloud services, IT, communciations

Would prefer to have life like images rather than animated.

I have included in the attachments a graphic we had designed for our digital marketing section which was specific to that topic. I don't want exactly the same but I like the concept. the new image is for a range of depts/topics and to go on an internal wall inside the business.

Could be one image that encompasses it all as in the attachment, or several pics merged together into one could include images of the related department eg: fleet tracking - truck, cell phone car kits - vehicle with cradle, IT Managed Services - computers, data and network cabling - ? , coverage extenders - vast land or a pic of dun-ro, m2m - m2m related pic, digital marketing - ?

Target Market(s)

Businesses

Font styles to use
Sans Serif

Requirements
Nice to have
• May include our logo or the varied logos of several distributors we use.

```html
<!DOCTYPE html>
<html lang="en">
<head>
<meta charset="utf-8">
<title>NKV Solutions – Wall Graphic</title>
<link rel="stylesheet" href="https://fonts.googleapis.com/css2?family=Raleway:wght@400;700&display=swap">
<style>
  :root {
    --canvas-bg: #e6e6e6;
    --wall-white: #ffffff;
    --brand-navy: #24356f;
    --brand-blue: #2b4a9b;
    --text-grey: #3a3a3a;
    --cable-blue: #2f7fc9;
    --map-red: #c9353a;
    --sky-gold: #e6a94a;
    --digital-teal: #1fa3a8;
  }
  html, body {
    margin: 0;
    padding: 0;
    width: 1200px;
    height: 1200px;
    overflow: hidden;
    background: var(--canvas-bg);
    font-family: "Raleway", Arial, sans-serif;
  }
  .wall-graphic {
    position: absolute;
    left: 0;
    top: 81px;
    width: 1200px;
    height: 1037px;
    background: var(--wall-white);
    overflow: hidden;
  }
  .brand {
    position: absolute;
    left: 86px;
    top: 300px;
    display: flex;
    align-items: center;
    gap: 12px;
    font-weight: 700;
    font-size: 30px;
    letter-spacing: 1px;
    color: var(--brand-navy);
  }
  .brand-dot {
    width: 20px;
    height: 20px;
    border-radius: 50%;
    background: var(--brand-navy);
  }
  .tagline {
    position: absolute;
    left: 73px;
    top: 440px;
    margin: 0;
    font-weight: 400;
    font-size: 46px;
    line-height: 51px;
    color: var(--brand-blue);
  }
  .tagline .tag-last { color: var(--text-grey); }
  .photo-strip {
    position: absolute;
    width: 173px;
  }
  .strip-cabling {
    left: 411px; top: 235px; height: 360px;
    background: linear-gradient(160deg, #1d5fa8, var(--cable-blue) 45%, #9cc6ea 85%, #ffffff);
  }
  .strip-carkit {
    left: 585px; top: 332px; height: 367px;
    background: linear-gradient(180deg, #f3f3f3, #8c8c8c 30%, var(--map-red) 55%, #6d6d6d 80%, #d9d9d9);
  }
  .strip-fleet {
    left: 760px; top: 270px; height: 367px;
    background: linear-gradient(180deg, #4e86b8, var(--sky-gold) 25%, #9aa6b0 45%, #c8333a 65%, #dcdcdc 90%, #ffffff);
  }
  .strip-digital {
    left: 933px; top: 319px; height: 380px;
    background: linear-gradient(160deg, #ffffff, var(--digital-teal) 25%, #1b4f8c 55%, #4ab84a 75%, #1b1f3a);
  }
  .network-band {
    position: absolute;
    left: 0;
    top: 700px;
    width: 1200px;
    height: 280px;
  }
  .web-address {
    position: absolute;
    left: 861px;
    top: 960px;
    font-size: 26px;
    color: var(--brand-blue);
  }
</style>
</head>
<body>
  <main class="wall-graphic">
    <div class="brand"><span class="brand-dot"></span><span class="brand-name">NKV SOLUTIONS</span></div>
    <h1 class="tagline">Innovative<br>Technology<br><span class="tag-last">Solutions</span></h1>

    <div class="photo-strip strip-cabling" role="img" aria-label="Close-up photo of a blue network cable connector"></div>
    <div class="photo-strip strip-carkit" role="img" aria-label="Photo of a smartphone with map navigation in a car cradle"></div>
    <div class="photo-strip strip-fleet" role="img" aria-label="Photo of a red fleet truck on a wet road under a sunset sky"></div>
    <div class="photo-strip strip-digital" role="img" aria-label="Photo of a hand holding a phone with glowing digital marketing icons"></div>

    <svg class="network-band" viewBox="0 0 1200 280" role="img" aria-label="Decorative ribbon of colourful connected network nodes">
      <defs>
        <linearGradient id="bandTone" x1="0" y1="0" x2="1" y2="0">
          <stop offset="0" stop-color="#2f9fd8" stop-opacity="0.35"/>
          <stop offset="0.3" stop-color="#1fa3a8" stop-opacity="0.35"/>
          <stop offset="0.55" stop-color="#2b4a9b" stop-opacity="0.3"/>
          <stop offset="0.8" stop-color="#4ab84a" stop-opacity="0.3"/>
          <stop offset="1" stop-color="#e0463c" stop-opacity="0.35"/>
        </linearGradient>
      </defs>
      <polygon points="30,200 1200,20 1200,90 40,270" fill="url(#bandTone)"/>
    </svg>

    <div class="web-address">www.website.com</div>
  </main>
</body>
</html>
```